Collaborative Business card design

I have a logo that I would like incorporate with my wife who is now a realtor as well.
Target Market(s)
Real Estate
Industry/Entity Type
Real Estate
Contact Information for Business Card
Names, Email accounts and phone numbers.. and Business info (required)
Font styles to use
Script
Colors
A7469A
B969AE
D3A5CF
EDDBEB
F8F0F9
Requirements
Must have
- Both Pictures and the logo from the previous business card

```html
<!DOCTYPE html>
<html lang="en">
<head>
<meta charset="utf-8">
<title>Marcus &amp; Elise Business Cards</title>
<link rel="stylesheet" href="https://fonts.googleapis.com/css2?family=Cinzel:wght@400;500&family=Pinyon+Script&family=Cabin:wght@400&display=swap">
<style>
  :root {
    --backdrop: #9c9ea3;
    --card-light: #f2f2f2;
    --plum: #56214a;
    --plum-text: #4a1540;
    --navy: #2b1c6e;
    --indigo: #2e1c6e;
    --indigo-deep: #1f1255;
    --white: #ffffff;
    --photo-top: #f4f4f6;
    --photo-mid: #b8a79a;
    --photo-low: #6a89c4;
  }
  * { margin: 0; padding: 0; box-sizing: border-box; }
  html, body { width: 1200px; height: 1000px; overflow: hidden; }
  body { background: var(--backdrop); position: relative; }

  .card { position: absolute; top: 263px; height: 468px; overflow: hidden; }

  /* Front card */
  .card--front { left: 264px; width: 303px; background: var(--card-light); }
  .brand {
    position: absolute; top: 68px; left: 0; width: 100%;
    text-align: center; font-family: "Cinzel", serif; font-weight: 500;
    color: var(--navy); line-height: 1.1;
  }
  .brand__mark {
    display: block; width: 58px; height: 58px; margin: 0 auto 28px;
    background: var(--navy);
  }
  .brand__name { display: block; font-size: 29px; }
  .brand__sub { display: block; font-size: 15px; letter-spacing: 3px; margin-top: 3px; }

  .services {
    position: absolute; top: 236px; left: 62px; list-style: none;
    font-family: "Cinzel", serif; font-weight: 500; font-size: 21px; color: var(--plum-text);
    line-height: 26px; letter-spacing: 0.3px;
  }
  .services li::before { content: "\2022"; font-size: 14px; margin-right: 8px; vertical-align: 3px; }

  .brokerage {
    position: absolute; left: 0; bottom: 0; width: 100%; height: 121px;
    background: var(--plum); color: var(--white);
    font-family: "Cinzel", serif; text-align: center;
  }
  .brokerage__seal {
    position: absolute; top: 20px; left: 50%; width: 38px; height: 38px;
    margin-left: -19px; border: 1.5px solid var(--white); border-radius: 50%;
  }
  .brokerage__name {
    position: absolute; top: 66px; left: 0; width: 100%;
    font-size: 13px; line-height: 15px;
  }

  /* Back card */
  .card--back { left: 689px; width: 300px; background: var(--indigo); }
  .portrait {
    position: absolute; top: 0; left: 0; width: 100%; height: 247px;
    background: linear-gradient(180deg, var(--photo-top) 0%, var(--photo-mid) 45%, var(--photo-low) 100%);
  }
  .names { position: absolute; top: 262px; left: 0; width: 100%; height: 80px; }
  .names__amp {
    position: absolute; top: -42px; left: 188px;
    font-family: "Pinyon Script", cursive; font-size: 112px; line-height: 1; color: var(--indigo-deep);
  }
  .names__first {
    position: absolute; top: 2px; left: 104px;
    font-family: "Cinzel", serif; font-size: 28px; line-height: 1; color: var(--white);
  }
  .names__second {
    position: absolute; top: 22px; left: 40px; width: 190px; text-align: center;
    font-family: "Pinyon Script", cursive; font-size: 60px; line-height: 1; color: var(--white);
  }
  .phone {
    position: absolute; top: 346px; left: 0; width: 100%; text-align: center;
    font-family: "Cinzel", serif; font-size: 28px; color: var(--white);
  }
  .emails {
    position: absolute; top: 397px; left: 0; width: 100%; text-align: center;
    font-family: "Cabin", sans-serif; font-size: 11.5px; line-height: 15px; color: var(--white);
  }
  .address {
    position: absolute; top: 440px; left: 0; width: 100%; text-align: center;
    font-family: "Cabin", sans-serif; font-size: 11px; color: var(--white);
  }
</style>
</head>
<body>
  <section class="card card--front">
    <div class="brand">
      <span class="brand__mark"></span>
      <span class="brand__name">Marcus Hale</span>
      <span class="brand__sub">Real Estate</span>
    </div>
    <ul class="services">
      <li>Residential</li>
      <li>Commercial</li>
      <li>Agricultural</li>
    </ul>
    <div class="brokerage">
      <span class="brokerage__seal"></span>
      <div class="brokerage__name">Summit Ridge Realty Group<br>Gem Valley Homes &amp; Properties</div>
    </div>
  </section>

  <section class="card card--back">
    <div class="portrait" role="img" aria-label="Portrait photo of the two agents, Marcus and Elise, side by side"></div>
    <div class="names">
      <span class="names__amp">&amp;</span>
      <span class="names__first">MARCUS</span>
      <span class="names__second">Elise</span>
    </div>
    <div class="phone">555-014-2391</div>
    <div class="emails">marcus@summitridgehomes.com<br>elise@summitridgehomes.com</div>
    <div class="address">820 Canyon Rim Rd Suite 110, Maple Falls Idaho 83399</div>
  </section>
</body>
</html>
```